Conference program advertisement

Our business www.clinicledger.com.au is a good sponsor of the conference program run by the Southern Pacific Guild of Perioperative Physicians (SPGPP) here in Western Australia.
We have been running the same ad for a while and so we could do with a fresh new presence.
We have a conference banner and other signage that we'll use at the trade show so we're not looking to rebrand. Just looking for a new ad.
Specification is full colour A4, high res PDF
(Because I'm using my phone to create this job, I cannot seem to upload the existing ad. I'll do do ASAP.)

Target Market(s)

Specialist doctors

Industry/Entity Type

Trade

Font styles to use
Sans Serif

Colors

Designer to choose colors to be used in the design.

Requirements
Must have
• A4
Existing logo and colour scheme

```html
<!DOCTYPE html>
<html lang="en">
<head>
<meta charset="utf-8">
<title>Clinic Ledger Services – Conference Advertisement</title>
<link rel="stylesheet" href="https://fonts.googleapis.com/css2?family=Roboto+Condensed:wght@700&family=Barlow:wght@500&family=Arimo:wght@400;700&display=swap">
<style>
  :root {
    --red: #c7283a;
    --ink: #231f20;
    --paper: #ffffff;
    --tile-edge: #d6d6d6;
    --tile-shade: #e9e9e9;
    --brand-square: #b9b9b9;
    --theatre-dark: #0d3b3a;
    --theatre-mid: #1f7a78;
    --theatre-light: #7fc6c4;
  }
  * { margin: 0; padding: 0; box-sizing: border-box; }
  html, body { width: 849px; height: 1200px; overflow: hidden; background: var(--paper); }
  .advert { position: relative; width: 849px; height: 1200px; overflow: hidden; background: var(--paper); color: var(--ink); }

  .hero-photo {
    position: absolute; left: 0; top: 0; width: 849px; height: 552px;
    background:
      radial-gradient(ellipse 260px 180px at 390px 400px, #e8f3f2 0%, rgba(232,243,242,0) 100%),
      radial-gradient(ellipse 420px 300px at 300px 300px, var(--theatre-light) 0%, rgba(127,198,196,0) 100%),
      linear-gradient(135deg, #6da9a6 0%, var(--theatre-mid) 45%, var(--theatre-dark) 100%);
  }

  .headline {
    position: absolute; left: 0; top: 566px; width: 849px;
    font-family: "Roboto Condensed", "Arial Narrow", sans-serif; font-weight: 700;
    font-size: 62px; line-height: 64px; letter-spacing: 0;
    text-transform: uppercase; color: var(--red); text-align: center;
  }
  .headline-line { display: block; white-space: nowrap; }
  .headline .dark { color: var(--ink); }

  .intro {
    position: absolute; left: 38px; top: 694px; width: 771px;
    font-family: "Barlow", Arial, sans-serif; font-weight: 500;
    font-size: 16.8px; line-height: 23.7px; letter-spacing: 0.3px;
    text-align: justify;
  }

  .service {
    position: absolute; display: flex; flex-direction: column; align-items: center; justify-content: center;
    text-align: center; white-space: nowrap;
    font-family: "Arimo", Arial, sans-serif; font-size: 14px; line-height: 19px;
    letter-spacing: 0.3px; text-transform: uppercase; color: var(--ink);
    background: linear-gradient(180deg, var(--paper) 0%, var(--paper) 70%, var(--tile-shade) 100%);
    border-top: 1px solid var(--tile-edge);
    box-shadow: inset 4px 0 0 var(--tile-shade), 0 2px 3px rgba(0,0,0,0.12);
  }
  .service.accent { color: var(--red); }
  .col-1 { left: 38px; width: 241px; }
  .col-2 { left: 305px; width: 240px; }
  .col-3 { left: 568px; width: 240px; }

  .contact {
    position: absolute; top: 1082px; font-style: normal;
    font-family: "Arimo", Arial, sans-serif; font-size: 14px; line-height: 19.5px; color: var(--ink);
    white-space: nowrap;
  }
  .contact strong { font-weight: 700; }
  .contact-primary { left: 38px; }
  .contact-secondary { left: 341px; top: 1086px; }

  .brand { position: absolute; left: 608px; top: 1076px; display: flex; align-items: center; gap: 12px; }
  .brand-square { width: 56px; height: 56px; background: var(--brand-square); border-radius: 6px; }
  .brand-name {
    font-family: "Arimo", Arial, sans-serif; font-weight: 400;
    font-size: 20px; line-height: 20px; text-transform: uppercase; color: var(--red);
  }
</style>
</head>
<body>
<main class="advert">
  <div class="hero-photo" role="img" aria-label="Surgical team in teal scrubs, caps and masks operating under theatre lights"></div>

  <h1 class="headline">
    <span class="headline-line">Is <span class="dark">administration</span> eating</span>
    <span class="headline-line">up your valuable time?</span>
  </h1>

  <p class="intro">Admin can consume a large amount of time for doctors working in private practice. From generating accounts to chasing up bad debts, from sitting on hold with health funds, or trawling through remittance advices to getting accreditation papers and submitting provider number applications properly - we’re sure you would prefer to focus on being a doctor rather than worrying about paperwork and piles of admin. Clinic Ledger Services is here to help - contact us today if you’re ready to remove the burden of admin.</p>

  <div class="service col-1" style="top:870px;height:30px;">Private billing</div>
  <div class="service col-1 accent" style="top:910px;height:30px;">VMP billing</div>
  <div class="service col-1" style="top:951px;height:30px;">Practice management</div>
  <div class="service col-1 accent" style="top:991px;height:30px;">Organise lists</div>
  <div class="service col-1" style="top:1031px;height:30px;">Cover lists</div>

  <div class="service col-2 accent" style="top:870px;height:30px;">Banking</div>
  <div class="service col-2" style="top:910px;height:71px;"><span>Medicare and health</span><span>fund registrations</span></div>
  <div class="service col-2 accent" style="top:991px;height:70px;"><span>Fee estimates and informed</span><span>financial consent</span></div>

  <div class="service col-3" style="top:870px;height:53px;"><span>Direct Bill and credit card</span><span>payments</span></div>
  <div class="service col-3 accent" style="top:933px;height:48px;"><span>Electronic claiming to</span><span>health funds</span></div>
  <div class="service col-3" style="top:991px;height:30px;">GST reporting</div>
  <div class="service col-3 accent" style="top:1031px;height:30px;">Hospital accreditations</div>

  <address class="contact contact-primary">
    <strong>Sam Whitlow</strong> Mobile +61 400 555 218<br>
    First Floor, Unit 12, 450 Harbour Street,<br>
    West Perth, WA, 6005
  </address>
  <address class="contact contact-secondary">
    PO Box 980, West Perth WA 6872<br>
    sam@clinicledger.com.au<br>
    www.clinicledger.com.au
  </address>

  <div class="brand">
    <div class="brand-square"></div>
    <div class="brand-name">Clinic<br>Ledger<br>Services</div>
  </div>
</main>
</body>
</html>
```